Dorsey K. Wendell Business Card

We need a business card for our company Dorsey K. Wendell Heating & Plumbing to be distributed to potential customers. It should follow the color scheme of our logo and have a modern upscale and masculine look.

The logo is attached and the info below should also be included:

5187 W. Cedar Brook Rd.
Alderton, PA 17688

Russell T. Wendell
(717) 592-0817
russelltwendell@fernmail.net
dorseykwendell.net
PA #093148

Industry/Entity Type

Business

Contact Information for Business Card

5187 W. Cedar Brook Rd.
Alderton, PA 17688

Russell T. Wendell
(717) 592-0817
russelltwendell@fernmail.net
dorseykwendell.net
PA #093148

Colors

Designer to choose colors to be used in the design.

Requirements
Must have
• Information above included

```html
<!DOCTYPE html>
<html lang="en">
<head>
<meta charset="utf-8">
<title>Dorsey K. Wendell Business Card</title>
<link rel="stylesheet" href="https://fonts.googleapis.com/css2?family=Oswald:wght@400;600;700&display=swap">
<style>
  :root {
    --brand-blue: #1a55a8;
    --brand-green: #a3cb38;
    --ink: #2b2b2b;
    --card-white: #ffffff;
    --page: #ffffff;
    --water-light: #a9c4cf;
    --water-mid: #3f93b3;
    --water-deep: #1c5f95;
  }
  * { box-sizing: border-box; margin: 0; padding: 0; }
  html, body {
    width: 1200px; height: 1200px; overflow: hidden;
    background: var(--page);
    font-family: "Oswald", "Arial Narrow", sans-serif;
  }
  .sheet { position: relative; width: 1200px; height: 1200px; }

  .card {
    position: absolute; left: 146px; width: 907px; height: 518px;
    border-radius: 34px; overflow: hidden;
    box-shadow: 0 4px 10px rgba(0,0,0,0.25);
  }
  .card--front { top: 52px; background: var(--card-white); }
  .card--back { top: 618px; }

  /* front */
  .brand-mark {
    position: absolute; right: 53px; top: 56px;
    display: flex; align-items: center; gap: 14px;
  }
  .brand-mark__square { width: 72px; height: 72px; background: var(--brand-blue); }
  .brand-mark__name {
    color: var(--brand-blue); font-weight: 600; font-size: 30px;
    line-height: 1.15; text-transform: uppercase; letter-spacing: 0.5px;
  }
  .license {
    position: absolute; right: 53px; top: 143px;
    font-size: 18px; color: var(--ink); font-weight: 400;
  }
  .contact { position: absolute; left: 53px; top: 232px; color: var(--ink); }
  .contact__name {
    font-size: 36px; font-weight: 600; color: var(--brand-blue);
    letter-spacing: 1.5px; line-height: 1.1; text-transform: uppercase;
  }
  .contact__title { font-size: 23px; font-weight: 400; letter-spacing: 0.8px; margin-top: 0; }
  .contact__address { font-size: 23px; line-height: 27px; margin-top: 14px; letter-spacing: 0.3px; }
  .contact__lines { list-style: none; margin-top: 14px; }
  .contact__lines li {
    display: flex; align-items: center; gap: 18px;
    font-size: 23px; line-height: 30px; letter-spacing: 0.4px;
  }
  .contact__lines svg { width: 22px; height: 22px; fill: var(--brand-blue); flex: none; }

  /* back */
  .water-photo {
    position: absolute; inset: 0;
    background:
      linear-gradient(172deg, var(--water-light) 0%, #9bbcc9 38%, var(--water-mid) 55%, #2f82a9 78%, var(--water-deep) 100%);
  }
  .back-brand {
    position: absolute; left: 0; right: 0; top: 206px;
    display: flex; justify-content: center; align-items: center; gap: 16px;
  }
  .back-brand__square { width: 86px; height: 86px; background: #ffffff; }
  .back-brand__name {
    color: #ffffff; font-weight: 600; font-size: 34px; line-height: 1.15;
    text-transform: uppercase; letter-spacing: 0.5px;
  }
  .services-tag {
    position: absolute; left: 352px; top: 350px; width: 205px; height: 43px;
    border-radius: 10px; background: var(--brand-green);
    color: #ffffff; font-weight: 700; font-size: 32px; line-height: 43px;
    text-align: center; letter-spacing: 0.5px;
  }
  .services-list {
    position: absolute; left: 0; right: 0; top: 418px;
    text-align: center; color: #ffffff; font-weight: 600; font-size: 26px;
  }
  .services-list .dot { color: var(--brand-green); margin: 0 8px; }
</style>
</head>
<body>
<main class="sheet">
  <section class="card card--front" aria-label="Business card front">
    <div class="brand-mark">
      <span class="brand-mark__square" aria-hidden="true"></span>
      <span class="brand-mark__name">Dorsey K. Wendell<br>Heating &amp; Plumbing</span>
    </div>
    <p class="license">PA #093148</p>

    <div class="contact">
      <h1 class="contact__name">Russell T. Wendell</h1>
      <p class="contact__title">Managing Director</p>
      <p class="contact__address">5187 W. Cedar Brook Rd.<br>Alderton, PA 17688</p>
      <ul class="contact__lines">
        <li>
          <svg viewBox="0 0 24 24" aria-hidden="true"><path d="M6.6 10.8a15.1 15.1 0 0 0 6.6 6.6l2.2-2.2a1 1 0 0 1 1-.25 11.4 11.4 0 0 0 3.6.57 1 1 0 0 1 1 1V20a1 1 0 0 1-1 1A17 17 0 0 1 3 4a1 1 0 0 1 1-1h3.5a1 1 0 0 1 1 1c0 1.25.2 2.45.57 3.57a1 1 0 0 1-.25 1z"/></svg>
          (717) 592-0817
        </li>
        <li>
          <svg viewBox="0 0 24 24" aria-hidden="true"><path d="M2 5h20l-10 7.5zM2 7v12l7-6zM22 7v12l-7-6zM10.3 14l1.7 1.3 1.7-1.3L22 19H2z"/></svg>
          russelltwendell@fernmail.net
        </li>
        <li>
          <svg viewBox="0 0 24 24" aria-hidden="true"><circle cx="12" cy="12" r="9.5" fill="none" stroke="#1a55a8" stroke-width="2.2"/><path d="M7 7.5c2 0 3 1.5 2.5 3s-2 1.5-2 3 1.5 2 1.5 4l-2.5-1.5C5 14 4.5 10 7 7.5zM14 5c1 1.5 0 2.5 1.5 3s3 0 3.5 2c-2 .5-2.5 2-2 4s-1.5 3-2.5 4c0-2-1.5-3-1.5-5s-2-2.5-1.5-4S13 6.5 14 5z"/></svg>
          www.dorseykwendell.net
        </li>
      </ul>
    </div>
  </section>

  <section class="card card--back" aria-label="Business card back">
    <div class="water-photo" role="img" aria-label="Photograph of a blue water splash wave with rising bubbles"></div>
    <div class="back-brand">
      <span class="back-brand__square" aria-hidden="true"></span>
      <span class="back-brand__name">Dorsey K. Wendell<br>Heating &amp; Plumbing</span>
    </div>
    <p class="services-tag">SERVICES</p>
    <p class="services-list">Service &amp; Repair<span class="dot">•</span>New Construction<span class="dot">•</span>Light Commercial</p>
  </section>
</main>
</body>
</html>
```